Brinevale Yacht Management Full Page Ad Flyer

Yacht Management Package also includes the following periodic Monthly services:

Monthly full vessel systems checklist inspections
Diver For Hull Cleaning And Inspection Of Props, Shafts, and Zincs
Interior/Exterior Detailing and scheduled washdowns
Manage Haulout
Pump-out Services
On-call Captain and Crew Services
Updates

Need more time to provide more content to designers and the printing press template file.

Target Market(s)

Vessel owners, motor yachts, sailboats from 25 feet in length up to 125 feet in length. We do not do cruise ships or yachts larger than 125 feet. Someone who has their boat docked at their house or a local marina. We also offer mobile on-site services.

```html
<!DOCTYPE html>
<html lang="en">
<head>
<meta charset="UTF-8">
<title>Brinevale Yacht Management – Full Page Ad</title>
<link href="https://fonts.googleapis.com/css2?family=Bebas+Neue&family=Delius&display=swap" rel="stylesheet">
<style>
  :root {
    --page-bg: #dde8ef;
    --sky-top: #5fb3e6;
    --sky-mid: #b9dff2;
    --sea: #a9d9d6;
    --sand: #f0d9a6;
    --navy: #2e3d64;
    --cyan: #22a7d2;
    --brand-blue: #2e3d64;
    --body-ink: #26303d;
    --service-red: #e6262f;
    --frame: #3b3b3b;
  }
  * { margin: 0; padding: 0; box-sizing: border-box; }
  html, body { width: 1200px; height: 1200px; overflow: hidden; }
  body { background: var(--page-bg); position: relative; font-family: "Delius", sans-serif; }

  .flyer {
    position: absolute;
    left: 222px; top: 68px;
    width: 755px; height: 1062px;
    overflow: hidden;
    background: linear-gradient(180deg, var(--sky-top) 0%, var(--sky-mid) 38%, var(--sea) 52%, var(--sand) 72%, var(--sand) 100%);
    box-shadow: 0 18px 30px rgba(40, 60, 80, 0.18);
  }
  .flyer-shapes { position: absolute; inset: 0; }
  .flyer-frame {
    position: absolute;
    left: 6px; top: 5px; right: 5px; bottom: 5px;
    border: 1px solid var(--frame);
    pointer-events: none;
  }

  .brand {
    position: absolute;
    left: 38px; top: 46px;
    width: 396px; height: 104px;
    display: flex; align-items: center; gap: 14px;
  }
  .brand-mark { width: 20px; height: 20px; border-radius: 50%; background: var(--brand-blue); flex: none; }
  .brand-name {
    display: flex; flex-direction: column;
    font-family: "Bebas Neue", sans-serif;
    color: var(--brand-blue);
  }
  .brand-name-main { font-size: 70px; line-height: 66px; letter-spacing: 4px; }
  .brand-name-sub { font-size: 30px; line-height: 30px; letter-spacing: 7px; }

  .intro {
    position: absolute;
    left: 34px; top: 197px;
    width: 584px;
    font-size: 14.4px; line-height: 17.3px;
    color: var(--body-ink);
    text-align: justify;
    letter-spacing: 0.4px;
  }

  .services { position: absolute; left: 34px; top: 332px; list-style: none; }
  .service {
    position: absolute; left: 0;
    white-space: nowrap;
    font-family: "Bebas Neue", sans-serif;
    font-size: 34px; line-height: 40px;
    color: var(--service-red);
    text-shadow: 0 0 3px rgba(255, 255, 255, 0.9);
  }
  .service-1 { top: 0; }
  .service-2 { top: 120px; }
  .service-3 { top: 281px; }
  .service-4 { top: 443px; }
  .service-5 { top: 524px; }
  .service-6 { top: 605px; }
</style>
</head>
<body>
  <article class="flyer">
    <svg class="flyer-shapes" width="755" height="1062" viewBox="0 0 755 1062">
      <defs>
        <linearGradient id="yachtTone" x1="0" y1="0" x2="0" y2="1">
          <stop offset="0" stop-color="#e9f3f8"/>
          <stop offset="0.45" stop-color="#c9dbe6"/>
          <stop offset="0.8" stop-color="#9fb8c8"/>
          <stop offset="1" stop-color="#4f8fa8"/>
        </linearGradient>
      </defs>
      <circle class="accent-cyan" cx="802" cy="273" r="153" fill="var(--cyan)"/>
      <circle class="accent-navy" cx="610" cy="0" r="168" fill="var(--navy)"/>
      <circle class="photo-ring" cx="733" cy="803" r="447" fill="none" stroke="var(--navy)" stroke-width="9" stroke-dasharray="0 1450 500 2000"/>
      <circle class="photo-ring-light" cx="728" cy="801" r="450" fill="none" stroke="#ffffff" stroke-width="3"/>
      <circle class="yacht-photo" cx="728" cy="801" r="447" fill="url(#yachtTone)" role="img" aria-label="Photo of a white motor yacht cruising toward the viewer, bow spray on blue water"/>
    </svg>
    <div class="flyer-frame"></div>

    <header class="brand">
      <span class="brand-mark"></span>
      <span class="brand-name">
        <span class="brand-name-main">Brinevale</span>
        <span class="brand-name-sub">Yacht Management</span>
      </span>
    </header>

    <p class="intro">Hiring a professional yacht management service ensures your vessel stays in peak condition with expert maintenance, regular inspections, and thorough cleaning. You save time by leaving detailing, haulout coordination, and pump-out services to professionals, allowing you to focus on enjoying your yacht. With on-call crew services and timely care, you gain peace of mind while protecting your yacht’s longevity and value.</p>

    <ul class="services">
      <li class="service service-1">Monthly full vessel systems checklist<br>inspections</li>
      <li class="service service-2">Diver for hull cleaning and<br>inspection of props,<br>shafts, and zincs</li>
      <li class="service service-3">Interior/Exterior<br>detailing and scheduled<br>washdowns</li>
      <li class="service service-4">Manage haulout</li>
      <li class="service service-5">Pump-out services</li>
      <li class="service service-6">On-call captain and<br>crew services</li>
    </ul>
  </article>
</body>
</html>
```